Young, modern, highly skilled carpenter needs business card design

I need a business card design for my construction business. Its called 'Pellwright Construction Solutions'. Im looking for a ultra modern design that incorporates P C S, the first letters of the name with only a subtle reference to carpentry. The design should reflect my high quality work and eye for detail. i have also uploaded some exmaple designs i like.

Industry/Entity Type

Construction

Requirements
Must have
• Name of business, my name, mobile number, ABN number, email address
Nice to have
• A logo incorporating the name of the business

```html
<!DOCTYPE html>
<html lang="en">
<head>
<meta charset="utf-8">
<title>Pellwright Construction Solutions – Business Card</title>
<link href="https://fonts.googleapis.com/css2?family=Roboto:wght@400;500;700&display=swap" rel="stylesheet">
<style>
  :root {
    --brand-blue: #0a9de0;
    --slate: #4a5157;
    --tint: #d3e8ee;
    --paper: #ffffff;
    --card-edge: #6b6b6b;
    --ink: #3d4247;
  }
  * { margin: 0; padding: 0; box-sizing: border-box; }
  html, body { width: 1200px; height: 900px; overflow: hidden; background: var(--paper); }
  body { position: relative; font-family: "Roboto", Arial, sans-serif; color: var(--ink); }

  .card {
    position: absolute; left: 403px; width: 384px; height: 234px;
    background: var(--paper); border: 1px solid var(--card-edge); overflow: hidden;
  }
  .card--front { top: 83px; }
  .card--back { top: 381px; }

  .dot-field { position: absolute; }
  .card--front .dot-field {
    left: 0; top: 0; width: 150px; height: 160px;
    background: radial-gradient(ellipse at 55% 30%, rgba(211,232,238,1) 0%, rgba(211,232,238,.75) 45%, rgba(211,232,238,0) 75%);
  }
  .card--back .dot-field {
    inset: 0;
    background: radial-gradient(ellipse at 50% 45%, rgba(211,232,238,1) 0%, rgba(211,232,238,.85) 50%, rgba(211,232,238,.2) 85%, rgba(211,232,238,0) 100%);
  }

  .wordmark { position: absolute; display: flex; flex-direction: column; align-items: center; font-weight: 700; text-transform: uppercase; line-height: 1; }
  .wordmark__square { display: block; background: currentColor; margin-bottom: 6px; }
  .wordmark__name { letter-spacing: .04em; }
  .wordmark__tag { letter-spacing: .06em; margin-top: 3px; }

  .card--front .wordmark { left: 0; right: 0; top: 14px; color: var(--brand-blue); }
  .card--front .wordmark__square { width: 40px; height: 40px; }
  .card--front .wordmark__name { font-size: 20px; }
  .card--front .wordmark__tag { font-size: 7.5px; }

  .holder { position: absolute; left: 0; right: 0; top: 115px; text-align: center; }
  .holder__name { font-size: 14px; font-weight: 700; color: var(--brand-blue); letter-spacing: .03em; }
  .holder__role { font-size: 12.5px; font-weight: 700; color: var(--ink); margin-top: 2px; letter-spacing: .03em; }

  .contact { position: absolute; left: 13px; top: 171px; list-style: none; font-size: 11.5px; }
  .contact li { display: flex; align-items: center; height: 18px; }
  .contact__icon {
    width: 13px; height: 13px; border-radius: 50%; background: var(--brand-blue);
    color: var(--paper); font-size: 8.5px; font-weight: 700;
    display: inline-flex; align-items: center; justify-content: center; margin-right: 5px;
  }
  .abn { position: absolute; right: 12px; top: 211px; font-size: 11.5px; }
  .abn__label { color: var(--brand-blue); font-weight: 700; }

  .card--back .wordmark { left: 0; right: 0; top: 52px; color: var(--brand-blue); }
  .card--back .wordmark__square { width: 70px; height: 70px; }
  .card--back .wordmark__name { font-size: 30px; }
  .card--back .wordmark__tag { font-size: 11px; }

  .brand-band { position: absolute; left: 0; top: 698px; width: 1200px; height: 202px; background: var(--brand-blue); }
  .brand-band .wordmark { top: 28px; width: 240px; }
  .brand-band .wordmark__square { width: 104px; height: 86px; margin-bottom: 10px; }
  .brand-band .wordmark__name { font-size: 34px; }
  .brand-band .wordmark__tag { font-size: 12.5px; margin-top: 5px; }
  .wordmark--slate { left: 68px; color: var(--slate); }
  .wordmark--white { left: 883px; color: var(--paper); }
</style>
</head>
<body>

  <section class="card card--front" aria-label="Business card front">
    <div class="dot-field" role="img" aria-label="Soft halftone dot pattern in pale blue"></div>
    <div class="wordmark">
      <span class="wordmark__square" aria-hidden="true"></span>
      <span class="wordmark__name">Pellwright</span>
      <span class="wordmark__tag">Construction Solutions</span>
    </div>
    <div class="holder">
      <p class="holder__name">Liam Carver</p>
      <p class="holder__role">Director</p>
    </div>
    <ul class="contact">
      <li><span class="contact__icon">A</span>27 Ashby Lane, Australia 3021</li>
      <li><span class="contact__icon">M</span>0412 555 018</li>
      <li><span class="contact__icon">E</span>info@pellwright.com.au</li>
    </ul>
    <p class="abn"><span class="abn__label">ABN:</span> 000 000 00000</p>
  </section>

  <section class="card card--back" aria-label="Business card back">
    <div class="dot-field" role="img" aria-label="Large halftone dot pattern in pale blue"></div>
    <div class="wordmark">
      <span class="wordmark__square" aria-hidden="true"></span>
      <span class="wordmark__name">Pellwright</span>
      <span class="wordmark__tag">Construction Solutions</span>
    </div>
  </section>

  <section class="brand-band" aria-label="Brand colour variations">
    <div class="wordmark wordmark--slate">
      <span class="wordmark__square" aria-hidden="true"></span>
      <span class="wordmark__name">Pellwright</span>
      <span class="wordmark__tag">Construction Solutions</span>
    </div>
    <div class="wordmark wordmark--white">
      <span class="wordmark__square" aria-hidden="true"></span>
      <span class="wordmark__name">Pellwright</span>
      <span class="wordmark__tag">Construction Solutions</span>
    </div>
  </section>

</body>
</html>
```